Etiketten-Design für Gin gesucht
Wahnsinnige Arbeit die Henrike hier abgeliefert hat. Es wurde nicht nur ein Etikett sondern ein Design für eine ganze Produkt-Linie erstellt. Bereits mit dem ersten Design war dies eines unserer Top-Designs und wurde dann perfekt weiterentwickelt. Viele Grüße und Danke für die super Zusammenarbeit. Tobias, Lutz, Ferdl
Zielgruppe
Habadere.
Wir sind ein Team aus drei bayerischen Hobby Brennern und werden unter der Marke 'Fern Brennerei' Anfang 2021 einen GIN auf den Markt bringen.
Der GIN wird schwerpunktmäßig online verkauft und sollte daher eine exklusiv-auffällige Optik haben um die Kunden zu beeindrucken.
Unsere Spirituosen erweitern traditionelle Rezepte mit regionalen Zutaten und bringen dies mit ihrer stilvollen Verpackung zum Ausdruck. Unser GIN ist eine Entdeckung für Leute, die schon alles kennen und Spirituosen auch pur genießen ohne Tonic oder andere Mixgetränke. Wir legen sehr viel Wert auf Qualität der Zutaten sowie Zeit und Geduld im Herstellungsprozess. Durch die handwerkliche Kunst des Destillierens bieten wir immer neue Erlebnisse für den Feinschmecker in kleinen limitieren Losgrößen.
So kommt es, dass wir Sonntags rund um den Hohen Sattel (Altdorf am Sattel - 95733) spazieren, dabei immer auf der Jagd nach neuen Zutaten sind und diese dem traditionellen Wacholder hinzufügen.
Im Gegensatz zu vielen anderen GIN Sorten, die weit über 30 Botanicals verwenden, setzen wir eine reduzierte Auswahl von maximal zehn zusätzlichen Zutaten ein, damit Kunden diesen puren und unverwechselbaren Geschmack genießen können (z.B. rosa Pfeffer, Korriander, Zitrone etc.). Zu Beginn besteht die Marke aus drei verschiedenen GIN Sorten und wird später um weitere Spirituosen wie Geiste und alkoholische Mischgetränke sowie Tonics erweitert. Auch Gläser und Merchandise Artikel soll es von uns geben. Jede GIN und Geist Variante besticht durch eine besondere Zutat, die Botanicals in unseren Spirituosen sind ohnehin auf wenige beschränkt, wodurch wir jedem Getränk eine besondere Note und einen speziellen Charakter verleihen.
Aufgabenstellung
Wir suchen ein GIN-Etikett dessen Design ausdrückt, dass es sich um einen handgemachten, hochwertigen und limitierten GIN handelt. Wir sind offen für puristische Entwürfe als auch für kreativ-künstlerische Ideen die auf die Flasche gebracht werden können.
Unser erster GIN wird den Namen „nine“ tragen, vielleicht kann man es geschrieben oder aber auch als „X“ für die römische zehn einbauen.
Vorschläge sind nicht auf ein einzelnes Etikett beschränkt, das Haupt-Etikett darf auch in verschiedene Abschnitte unterteilt werden, wie es in den Anlagen bspw. zu sehen ist. Zudem freuen wir uns über Entwürfe zum Etikett der Flaschenrückseite sowie den Flaschenhals.
Da weitere Spirituosen (nicht nur GIN) folgen, soll das Etikett einen großen Wiedererkennungswert haben und sich bspw. der Spirituosen-Name einfach austauschen lassen oder sich 'nur' durch individuelle Farbgebung unterscheiden.
Je nach Umsetzung können Etiketten im Folientransferdruck hergestellt werden. Unser Logo kann, muss aber nicht zwangsläufig auf dem Hauptetikett zu finden sein.
Unser Schwerpunkt liegt regional in Bayreuth, Feinkostland Nordgau und am Hohen Sattel (95733 Altdorf am Sattel).
Es darf in das Etikett auch gerne eine Art „Skala“, hinten oder vorne eingebaut werden, je nach Design für bestimmte Ausprägung der Geschmacksrichtung, hier die folgenden Kategorien und in der Anlage ist auch ein Beispiel zu finden.
Kategorien
Wacholder, blumig, fruchtig, würzig

```html
<!DOCTYPE html>
<html lang="de">
<head>
<meta charset="utf-8">
<title>nine Gin – Etikettenlinie</title>
<link rel="stylesheet" href="https://fonts.googleapis.com/css2?family=Montserrat:wght@300;800&family=Pathway+Gothic+One&display=swap">
<style>
  :root {
    --paper: #ffffff;
    --glass: #f1f2f3;
    --amber-light: #f39a3a;
    --amber-mid: #e0521a;
    --amber-deep: #a52a08;
    --name-grey: #b9b9b9;
    --name-light: #f7c8a8;
    --sat-green: #1a8a6a;
    --oak-gold: #f6b21f;
    --dry-red: #c8101c;
    --scale-ink: #8a8a8a;
    --scale-ink-light: #fbe3c8;
    --tag-grey: #d9d9d9;
    --tag-cream: #fbe6cc;
    --tag-ink: #555555;
  }
  * { margin: 0; padding: 0; box-sizing: border-box; }
  html, body { width: 1200px; height: 1057px; overflow: hidden; background: var(--paper); }
  .canvas { position: relative; width: 1200px; height: 1057px; }

  .label { position: absolute; overflow: hidden; }
  .label svg { position: absolute; inset: 0; width: 100%; height: 100%; }
  .label--sat { left: 42px; top: 175px; width: 335px; height: 855px; background: var(--glass); }
  .label--oak { left: 465px; top: 175px; width: 335px; height: 855px;
    background: linear-gradient(105deg, var(--amber-light) 0%, var(--amber-mid) 45%, var(--amber-deep) 100%); }
  .label--dry { left: 900px; top: 30px; width: 275px; height: 1000px; background: var(--glass); }

  .brand-name { font-family: "Montserrat", sans-serif; font-weight: 800; font-size: 64px; fill: var(--name-grey); }
  .label--oak .brand-name { fill: var(--name-light); }
  .variant { font-family: "Montserrat", sans-serif; font-size: 15px; }
  .variant .bold { font-weight: 800; }
  .variant .light { font-weight: 300; }
  .scale-label { font-family: "Montserrat", sans-serif; font-weight: 300; font-size: 7.5px; fill: var(--scale-ink); }
  .label--oak .scale-label { fill: var(--scale-ink-light); }
  .scale-line { stroke: var(--scale-ink); stroke-width: .7; fill: var(--glass); }
  .label--oak .scale-line { stroke: var(--scale-ink-light); fill: none; }

  .tag {
    position: absolute; bottom: 0; left: 50%; transform: translateX(-50%);
    width: 60px; height: 132px; border-radius: 14px 14px 10px 10px;
    background: var(--tag-grey); color: var(--tag-ink);
    font-family: "Pathway Gothic One", sans-serif; font-size: 12.5px; line-height: 1.35;
    text-align: center; padding-top: 6px;
  }
  .label--oak .tag { background: var(--tag-cream); }
  .tag .hand { font-size: 19px; line-height: 1.05; letter-spacing: -.5px; }
</style>
</head>
<body>
<main class="canvas">

  <!-- SAT GIN -->
  <section class="label label--sat">
    <svg viewBox="0 0 335 855">
      <text class="brand-name" x="168" y="565" text-anchor="middle">nine</text>
      <text class="variant" fill="var(--sat-green)" transform="translate(95 450) rotate(-22)" letter-spacing="14">
        <tspan class="bold">SAT</tspan><tspan class="light"> GIN</tspan>
      </text>
      <g transform="translate(225 645) rotate(-22)">
        <text class="scale-label" x="-6" y="3" text-anchor="end">WACHOLDER</text>
        <text class="scale-label" x="-6" y="17" text-anchor="end">FLORAL</text>
        <text class="scale-label" x="-6" y="31" text-anchor="end">FRUCHTIG</text>
        <text class="scale-label" x="-6" y="45" text-anchor="end">GEWÜRZE</text>
        <g class="scale-line">
          <path d="M0 0H88M0 14H88M0 28H88M0 42H88"/>
          <circle cx="0" cy="0" r="3"/><circle cx="22" cy="0" r="3"/><circle cx="44" cy="0" r="3"/><circle cx="66" cy="0" r="3"/>
          <circle cx="0" cy="14" r="3"/><circle cx="44" cy="14" r="3"/><circle cx="66" cy="14" r="3"/><circle cx="88" cy="14" r="3"/>
          <circle cx="0" cy="28" r="3"/><circle cx="22" cy="28" r="3"/><circle cx="44" cy="28" r="3"/><circle cx="88" cy="28" r="3"/>
          <circle cx="0" cy="42" r="3"/><circle cx="22" cy="42" r="3"/><circle cx="66" cy="42" r="3"/><circle cx="88" cy="42" r="3"/>
        </g>
        <g fill="var(--sat-green)">
          <circle cx="88" cy="0" r="3.4"/><circle cx="22" cy="14" r="3.4"/><circle cx="66" cy="28" r="3.4"/><circle cx="44" cy="42" r="3.4"/>
        </g>
      </g>
    </svg>
    <div class="tag">700ml<br>Alc. 43%vol.<br>Batch-No.<br><span class="hand">003/166</span><br>Vintage<br><span class="hand">12/2020</span></div>
  </section>

  <!-- OAK GIN -->
  <section class="label label--oak">
    <svg viewBox="0 0 335 855">
      <text class="brand-name" x="168" y="565" text-anchor="middle">nine</text>
      <text class="variant" fill="var(--oak-gold)" transform="translate(95 450) rotate(-22)" letter-spacing="14">
        <tspan class="bold">OAK</tspan><tspan class="light"> GIN</tspan>
      </text>
      <g transform="translate(225 645) rotate(-22)">
        <text class="scale-label" x="-6" y="3" text-anchor="end">WACHOLDER</text>
        <text class="scale-label" x="-6" y="17" text-anchor="end">FLORAL</text>
        <text class="scale-label" x="-6" y="31" text-anchor="end">FRUCHTIG</text>
        <text class="scale-label" x="-6" y="45" text-anchor="end">GEWÜRZE</text>
        <g class="scale-line">
          <path d="M0 0H88M0 14H88M0 28H88M0 42H88"/>
          <circle cx="0" cy="0" r="3"/><circle cx="22" cy="0" r="3"/><circle cx="44" cy="0" r="3"/><circle cx="66" cy="0" r="3"/>
          <circle cx="0" cy="14" r="3"/><circle cx="44" cy="14" r="3"/><circle cx="66" cy="14" r="3"/><circle cx="88" cy="14" r="3"/>
          <circle cx="0" cy="28" r="3"/><circle cx="22" cy="28" r="3"/><circle cx="44" cy="28" r="3"/><circle cx="88" cy="28" r="3"/>
          <circle cx="0" cy="42" r="3"/><circle cx="22" cy="42" r="3"/><circle cx="66" cy="42" r="3"/><circle cx="88" cy="42" r="3"/>
        </g>
        <g fill="var(--oak-gold)">
          <circle cx="88" cy="0" r="3.4"/><circle cx="22" cy="14" r="3.4"/><circle cx="66" cy="28" r="3.4"/><circle cx="44" cy="42" r="3.4"/>
        </g>
      </g>
    </svg>
    <div class="tag">700ml<br>Alc. 43%vol.<br>Batch-No.<br><span class="hand">003/166</span><br>Vintage<br><span class="hand">12/2020</span></div>
  </section>

  <!-- DRY GIN -->
  <section class="label label--dry">
    <svg viewBox="0 0 275 1000">
      <text class="variant" fill="var(--dry-red)" x="137" y="375" text-anchor="middle" letter-spacing="11">
        <tspan class="bold">DRY</tspan><tspan class="light"> GIN</tspan>
      </text>
      <text class="brand-name" x="137" y="560" text-anchor="middle">nine</text>
      <g transform="translate(168 767)">
        <text class="scale-label" x="-108" y="3">WACHOLDER</text>
        <text class="scale-label" x="-108" y="13">FLORAL</text>
        <text class="scale-label" x="-108" y="23">FRUCHTIG</text>
        <text class="scale-label" x="-108" y="33">GEWÜRZE</text>
        <g class="scale-line">
          <path d="M-45 0H70M-45 10H70M-45 20H70M-45 30H70"/>
          <circle cx="-45" cy="0" r="2.6"/><circle cx="-16" cy="0" r="2.6"/><circle cx="13" cy="0" r="2.6"/><circle cx="42" cy="0" r="2.6"/>
          <circle cx="-45" cy="10" r="2.6"/><circle cx="13" cy="10" r="2.6"/><circle cx="42" cy="10" r="2.6"/><circle cx="70" cy="10" r="2.6"/>
          <circle cx="-45" cy="20" r="2.6"/><circle cx="-16" cy="20" r="2.6"/><circle cx="13" cy="20" r="2.6"/><circle cx="70" cy="20" r="2.6"/>
          <circle cx="-45" cy="30" r="2.6"/><circle cx="-16" cy="30" r="2.6"/><circle cx="42" cy="30" r="2.6"/><circle cx="70" cy="30" r="2.6"/>
        </g>
        <g fill="var(--dry-red)">
          <circle cx="70" cy="0" r="2.8"/><circle cx="-16" cy="10" r="2.8"/><circle cx="42" cy="20" r="2.8"/><circle cx="13" cy="30" r="2.8"/>
        </g>
      </g>
    </svg>
    <div class="tag">700ml<br>Alc. 43%vol.<br>Batch-No.<br><span class="hand">003/166</span><br>Vintage<br><span class="hand">12/2020</span></div>
  </section>

</main>
</body>
</html>
```